Musical Instrument Store Needs Band Instrument Postcard to Upgrade Current Customers

We need a new postcard design to mail to our current instrument rental customers. People start out renting a student line/beginner instrument and we want to emphasize our upgrade program that allows them to apply the equity from their beginner instrument to an intermediate or professional instrument. I have attached an image of the front (Velmora Postcard Front) and back (Velmora Postcard Back) of what we have used in the past. The back still needs to have all the information currently on it. The front can be whatever you come up with (I don't necessarily care for our current design), but should include the tagline "Reach Your Full Potential". Also, if there is more room on the front or back, it would be nice to have a brief mention of our lesson studio (I have also included our lesson studio postcard for ideas).

There are also pictures of each instrument attached. There are a few for the trumpet so you can decide which one would work best.

Target Market(s)

Current instrument rental customers

Industry/Entity Type

Store

Requirements
Must have
• The back of postcard must have all the information from the file "Velmora Postcard Back". The front should have the tagline "Reach Your Full Potential". Pictures of the instruments should be on the front as well.
Nice to have
• A brief mention or reminder that we have a large lesson studio with highly qualified instructors.

```html
<!DOCTYPE html>
<html lang="en">
<head>
<meta charset="utf-8">
<title>Velmora Postcard Front and Back</title>
<link href="https://fonts.googleapis.com/css2?family=Barlow:wght@400;500;700&family=Barlow+Condensed:wght@600&display=swap" rel="stylesheet">
<style>
  :root {
    --page: #d6d6d6;
    --card: #ffffff;
    --ink: #111111;
    --ink-soft: #1c1c1c;
    --head-light: #8a8a8a;
    --head-dark: #141414;
    --silver: #cfd2d6;
    --silver-deep: #9ea3a9;
    --brass: #d9b25a;
    --brass-deep: #b98d2f;
    --ebony: #26222b;
  }
  * { margin: 0; padding: 0; box-sizing: border-box; }
  html, body { width: 920px; height: 1200px; overflow: hidden; }
  body { background: var(--page); font-family: "Barlow", Arial, sans-serif; color: var(--ink); position: relative; }

  .postcard { position: absolute; left: 20px; width: 880px; background: var(--card); box-shadow: 0 2px 6px rgba(0,0,0,.25); overflow: hidden; }
  .postcard--front { top: 24px; height: 570px; }
  .postcard--back { top: 611px; height: 571px; }

  .instrument { position: absolute; border-radius: 10px; }
  .instrument--silver { background: linear-gradient(135deg, var(--silver), var(--silver-deep)); }
  .instrument--brass { background: linear-gradient(135deg, var(--brass), var(--brass-deep)); }
  .instrument--ebony { background: linear-gradient(90deg, var(--ebony), #4a4550); }

  /* front: instruments framing the headline */
  .front-trumpet-top { left: 20px; top: 0; width: 590px; height: 56px; border-radius: 0 0 12px 12px; }
  .front-clarinet { left: 142px; top: 64px; width: 512px; height: 46px; border-radius: 23px; }
  .front-slide-top { left: 672px; top: 0; width: 74px; height: 54px; border-radius: 0 0 18px 18px; }
  .front-flute-corner { left: 840px; top: 0; width: 24px; height: 104px; border-radius: 0 0 8px 8px; }
  .front-sax-neck { left: 0; top: 100px; width: 132px; height: 270px; border-radius: 0 40px 0 0; }
  .front-sax-bell { left: 0; top: 366px; width: 216px; height: 204px; border-radius: 0 70px 0 0; }
  .front-flute { left: 10px; top: 190px; width: 28px; height: 380px; border-radius: 8px 8px 0 0; opacity: .85; }
  .front-trumpet-right { left: 716px; top: 12px; width: 150px; height: 480px; border-radius: 30px 30px 60px 60px; }
  .front-clarinet-edge { left: 852px; top: 140px; width: 28px; height: 262px; border-radius: 14px 0 0 14px; }
  .front-trombone-bell { left: 575px; top: 372px; width: 138px; height: 140px; border-radius: 70px 20px 20px 70px; }
  .front-trombone-body { left: 205px; top: 452px; width: 675px; height: 118px; border-radius: 40px 0 0 40px; }

  .tagline { position: absolute; left: 180px; width: 520px; top: 176px; text-align: center;
    font-family: "Barlow Condensed", "Arial Narrow", sans-serif; font-weight: 600;
    font-size: 106px; line-height: 94px; text-transform: uppercase; letter-spacing: -1px; }
  .tagline span { display: inline-block; white-space: nowrap;
    background: linear-gradient(180deg, var(--head-light), var(--head-dark));
    -webkit-background-clip: text; background-clip: text; color: transparent; }

  /* back */
  .back-clarinet { left: 22px; top: 28px; width: 36px; height: 528px; border-radius: 16px; }

  .store { position: absolute; left: 93px; top: 38px; }
  .store__name { font-weight: 700; font-size: 32px; line-height: 40px; color: var(--ink); margin-bottom: 26px; }
  .store__contact { font-style: normal; font-weight: 500; font-size: 14.5px; line-height: 19px; color: var(--ink-soft); }

  .offer { position: absolute; left: 93px; top: 219px; width: 322px; font-size: 16px; line-height: 23px; color: var(--ink-soft); font-weight: 500; }
  .offer p + p { margin-top: 12px; }

  .studio { position: absolute; left: 93px; top: 466px; list-style: none; font-weight: 500; font-size: 19px; line-height: 37px; color: var(--ink); }
</style>
</head>
<body>
  <section class="postcard postcard--front" aria-label="Velmora Postcard Front">
    <div class="instrument instrument--silver front-trumpet-top" role="img" aria-label="Silver trumpet with brass valves lying horizontally"></div>
    <div class="instrument instrument--ebony front-clarinet" role="img" aria-label="Black clarinet lying horizontally"></div>
    <div class="instrument instrument--brass front-slide-top" role="img" aria-label="Brass slide section"></div>
    <div class="instrument instrument--silver front-flute-corner" role="img" aria-label="Flute head joint"></div>
    <div class="instrument instrument--silver front-sax-neck" role="img" aria-label="Silver alto saxophone neck and keys"></div>
    <div class="instrument instrument--silver front-sax-bell" role="img" aria-label="Silver alto saxophone bell"></div>
    <div class="instrument instrument--silver front-flute" role="img" aria-label="Silver flute standing vertically"></div>
    <div class="instrument instrument--silver front-trumpet-right" role="img" aria-label="Silver trumpet standing bell down"></div>
    <div class="instrument instrument--ebony front-clarinet-edge" role="img" aria-label="Clarinet bell at the edge"></div>
    <div class="instrument instrument--brass front-trombone-bell" role="img" aria-label="Brass trombone bell"></div>
    <div class="instrument instrument--brass front-trombone-body" role="img" aria-label="Brass trombone body and slide lying horizontally"></div>
    <h1 class="tagline"><span>Reach Your</span><br><span>Full Potential</span></h1>
  </section>

  <section class="postcard postcard--back" aria-label="Velmora Postcard Back">
    <div class="instrument instrument--ebony back-clarinet" role="img" aria-label="Black clarinet standing vertically"></div>
    <div class="store">
      <div class="store__name">Velmora Music Center</div>
      <address class="store__contact">
        2180 Larkfield Ave. NW<br>
        Brookhaven, OH 44902<br>
        330-555-0142<br>
        877-555-0142 (toll free)
      </address>
    </div>
    <div class="offer">
      <p>Your student is ready to Step-Up to a Soloist Performance Instrument. To make it easier, you may apply equity from the instrument you are currently renting towards the upgraded Soloist Performance or Artist Series Instrument.</p>
      <p>Please call to set up your private appointment.</p>
    </div>
    <ul class="studio">
      <li>LARGE LESSON STUDIO!</li>
      <li>HIGHLY QUALIFIED INSTRUCTORS!</li>
    </ul>
  </section>
</body>
</html>
```